Design a Dynamic and User-Friendly Website for kLobbyra: Revolutionize Visitor Management

Description of kLobbyra:

kLobbyra is an innovative online visitor management system designed to streamline the process of managing visitors in various organizational settings. Our system automates the check-in process, enhances security by keeping accurate visitor logs, and ensures compliance with local regulations through customizable features. With functionalities such as contactless sign-in, real-time notifications, visitor badge printing, and comprehensive reporting, kLobbyra provides a modern solution to traditional visitor management challenges.

Target Audience:

Our primary target audience includes businesses and institutions across Africa, starting with Nigeria. This includes corporate offices, educational institutions, healthcare facilities, and government buildings that are looking for efficient, secure, and scalable visitor management solutions. Our system is particularly tailored to meet the needs of facility managers, security personnel, and front desk staff who prioritize ease of use, data security, and operational efficiency. Additionally, kLobbyra aims to cater to IT managers looking for robust systems that can seamlessly integrate with existing organizational infrastructure.

Color Scheme:

While specific colors are not mandated, the chosen palette should convey trust and stability, growth and efficiency, and maintain a professional and clean appearance. The colors selected should harmonize to create a welcoming, secure, and efficient atmosphere.
Typography:

Use modern, sans-serif fonts for readability and a contemporary look. Primary text should be clear with high contrast against the background, and headings can be bold to create a hierarchical structure that is easy to navigate.
Imagery:

Photography: High-quality images that feature African professionals and contexts, illustrating diverse, professional scenarios relevant to our target industries (such as corporate offices, educational institutions, healthcare facilities). Photos should authentically represent the African demographic, showing interactions between people and technology, emphasizing the ease and security of the visitor management process.
Illustrations: Custom illustrations that should culturally resonate with African settings and characters, vividly depicting functionalities of kLobbyra such as scanning a QR code, receiving a visitor badge, or receiving alerts on a smartphone or desktop. These illustrations should adopt a style that complements the overall design aesthetic of the site.
Layout and Design Elements:

A clean, minimalistic layout that focuses on usability with easy navigation paths for all user types.
Use cards or tiles for different sections such as features, testimonials, or case studies, which can help organize information cleanly and attractively.
Consider interactive elements like hover effects, animated transitions for loading elements, and subtle animations in illustrations to make the user experience dynamic and engaging.
Overall Theme:

The theme should be professional and welcoming, reflecting a high-tech solution that is approachable for users with varying levels of tech expertise. The design should instill confidence in the security and efficiency of the system, while also being culturally appropriate and user-friendly to encourage interaction and exploration of the site’s content.
This style and theme guide emphasizes flexibility in color usage while maintaining clear directives on the emotional and functional responses the design should invoke, ensuring it aligns with the values and needs of kLobbyra's target audience.

What websites can designers draw inspiration from?
List websites you like and describe what you like about them.

https://tallodesk.com/en-usremove
same industry so you can see their approaches to marketing to similar customers - granted their target is not specific to african market Very clean design and straight to the point. Their feature set is closest to our feature set.
http://www.gatrumo.comremove
clean design and straight to the point
http://vennatrak.comremove

Home Page
-------------------
Main Goal: Encourage visitors to start their 15-day free trial, effectively converting them into leads or potential customers.

Content Layout:
Hero Section: Engaging hero image or video that shows the kLobbyra system in action, with clear, prominent call-to-action (CTA) buttons for "Start your 15 day free trial" and secondary CTA for "Buy now"

Product Overview: Quick introduction to what kLobbyra is and its key benefits, such as enhanced security, easy integration, and improved operational efficiency.

Features Highlight: Brief visuals or icons depicting major features like contactless sign-in, real-time alerts, and comprehensive reporting.

How It Works: A concise step-by-step guide or graphic explaining how to get started with kLobbyra.

CTA Section: A more detailed call to action for starting the free trial,
if they want a more hands on guide allow them to schedule a demo and if they are ready click purchase to buy now.
Footer: Navigation links to other site sections, social media links, and legal information.

-------------------
Pricing Page
-------------------
Main Goal: Clearly convey the pricing structure in a way that users can easily understand and compare options based on their location and specific needs.

Content Layout:

Pricing Introduction: Explain the subscription model, highlighting the flexibility and scalability of the service (i.e., per location and additional tablets).

Country-Specific Pricing Tabs: Tabs or a dropdown menu allowing users to choose their country (Nigeria, Ghana, South Africa, Kenya) to view localized pricing in the respective currencies (NGN, GHS, ZAR, KES).
Subscription Per Location: Detailed pricing for managing a single location, with benefits listed beside the price

Tablets and Data Plans: A clear breakdown of the cost per tablet and the associated wireless data plans, including bulk discount options if applicable.
Interactive Pricing Calculator: A tool that allows users to calculate their monthly cost based on the number of locations and tablets they plan to use.

Add ons - for hardware, etc

FAQs: A section dedicated to frequently asked questions specifically about pricing, billing cycles, and cancellation policies.

CTA: Strong call to action for starting a free trial, with an emphasis on the ease of signing up and the no-commitment nature of the trial.

Footer: Standard navigational links, contact information, and social media buttons.

-------------------
Feature Page Template
-------------------
Main Goal: To detail individual features of kLobbyra, demonstrating the functionality and benefits to help prospective clients understand the value provided.

Content Layout:
Feature Introduction: Large title with a succinct description of the feature.

In-depth Details: Bullet points or short paragraphs explaining the feature, supported by relevant images or icons.

Use Case Scenario: Real-world application or a mini-case study showing the feature in action.

Benefit Summary: A list or graphic illustrating the benefits of the feature.

CTA: Prompt to try this feature via signup or schedule a demo speak with a sales representative.

Footer: Standard links and social media connections.

-------------------
Blog Page
-------------------
Main Goal: To engage current and prospective clients with useful content, position kLobbyra as a thought leader in the visitor management space, and improve SEO rankings.

Content Layout:
Featured Article: Highlight a recent or popular post prominently at the top.

Article List: Thumbnails and summaries of additional articles with clear categorization (e.g., Tips, Case Studies, Industry News).

Search and Filter Tools: Allow users to filter blog posts by topic, date, etc.

Newsletter Signup: Encourage visitors to subscribe to updates.
Social Share Buttons: Enable easy sharing of articles.
Footer: Include a comprehensive footer with navigational links and contact info.

Generic Content Page (e.g., Contact Us, About Us)
------------------------------
Main Goal: To provide essential information about the kLobbyra company or to facilitate contact with the company.

Content Layout:
Page Title and Introduction: Clear heading with a brief paragraph summarizing the page’s purpose.

Main Content Area: Detailed content appropriate to the page (e.g., company history, team bios for About Us; contact form, map, and helpline numbers for Contact Us).

Sidebar/Additional Elements: For Contact Us, include operational hours or a quick FAQ. For About Us, list awards or recognitions.

CTA: Depending on the page, direct users to other parts of the site (e.g., careers page link on About Us, newsletter sign-up on Contact Us).
Footer: Standard footer with expanded company details if on the Contact Us page.

Coding

```html
<!DOCTYPE html>
<html lang="en">
<head>
<meta charset="utf-8">
<title>kLobbyra — Online Visitor Management</title>
<link rel="stylesheet" href="https://fonts.googleapis.com/css2?family=DM+Sans:wght@400;500;600;700&family=Lato:wght@400;700;900&display=swap">
<style>
:root{
  --blue:#1d72d8;
  --blue-dark:#165fb6;
  --hero-bg:#e5effb;
  --soft-bg:#ebf3fc;
  --ink:#1d1d1f;
  --text:#3a3a3a;
  --muted:#555;
  --line:#d8e3f1;
  --grey-band:#ececec;
  --footer-bottom:#0e2a4d;
  --star:#f5a623;
}
*{margin:0;padding:0;box-sizing:border-box}
html,body{width:1200px;height:4216px;overflow:hidden}
body{position:relative;background:#fff;font-family:"Lato",sans-serif;color:var(--text)}
.abs{position:absolute}
.btn{position:absolute;display:flex;align-items:center;justify-content:center;border-radius:20px;font-family:"DM Sans",sans-serif;font-size:12.5px;font-weight:500;background:var(--blue);color:#fff;z-index:2}
.btn-outline{background:transparent;border:2px solid var(--blue);color:var(--blue)}
.photo{position:absolute}
.section-title{position:absolute;left:0;width:1200px;text-align:center;font-family:"Lato",sans-serif;font-weight:700;font-size:46px;color:var(--ink)}
.title-rule{position:absolute;left:558px;width:85px;height:3px;background:var(--blue);border-radius:2px}

/* header + hero */
.hero{position:absolute;left:0;top:0;width:1200px;height:586px;background:var(--hero-bg)}
.brand{position:absolute;display:flex;align-items:center;gap:10px;font-family:"DM Sans",sans-serif;font-weight:500;color:var(--blue)}
.brand .dot{border-radius:50%;border:4px solid currentColor}
.nav a{position:absolute;top:40px;font-family:"DM Sans",sans-serif;font-size:12.5px;color:#333;text-decoration:none}
.nav a.active{font-weight:700;color:#111}
.hero h1{position:absolute;left:141px;top:202px;width:480px;font-family:"DM Sans",sans-serif;font-size:31px;line-height:54px;font-weight:600;color:var(--ink);z-index:2}
.hero p{position:absolute;left:141px;top:316px;width:470px;font-size:13.3px;line-height:26px;color:#222;z-index:2}
.scroll-badge{position:absolute;left:576px;top:559px;width:48px;height:48px;border-radius:50%;background:#fff;display:flex;align-items:center;justify-content:center}
.scroll-badge span{width:36px;height:36px;border-radius:50%;background:var(--blue);display:flex;align-items:center;justify-content:center}

/* about */
.about-title{position:absolute;left:619px;top:720px;font-size:23px;font-weight:700;color:var(--ink)}
.about-copy{position:absolute;left:619px;width:425px;font-size:12.3px;line-height:25.4px;color:#333}

/* features */
.features{position:absolute;left:0;top:1306px;width:1200px;height:714px;background:var(--soft-bg)}
.feature-card{position:absolute;left:652px;width:365px;height:113px;background:#fff;box-shadow:0 2px 8px rgba(30,70,130,.08)}
.feature-card h3{position:absolute;font-size:17px;font-weight:700;color:var(--ink)}
.feature-card p{position:absolute;width:250px;font-size:11.5px;line-height:19.5px;color:#333}
.icon-disc{position:absolute;width:68px;height:68px;border-radius:50%;background:#f1f1f1;display:flex;align-items:center;justify-content:center}

/* steps */
.step-ring{position:absolute;top:2205px;width:140px;height:140px;border-radius:50%;border:1.5px dashed #9cc1ec}
.step-core{position:absolute;top:2221px;width:108px;height:108px;border-radius:50%;background:#fff;box-shadow:0 4px 14px rgba(0,0,0,.12);display:flex;align-items:center;justify-content:center}
.step-num{position:absolute;top:2296px;width:38px;height:38px;border-radius:50%;background:var(--blue);color:#fff;font-weight:700;font-size:17px;display:flex;align-items:center;justify-content:center}
.step-title{position:absolute;top:2354px;width:260px;text-align:center;font-size:17px;color:var(--ink)}
.step-copy{position:absolute;top:2383px;width:210px;text-align:center;font-size:12.3px;line-height:19.5px;color:#444}

/* cta band */
.cta-band{position:absolute;left:0;top:2609px;width:1200px;height:421px;background:var(--grey-band)}
.cta-copy{position:absolute;left:0;top:2609px;width:589px;height:421px}
.cta-copy h2{position:absolute;left:142px;top:108px;width:440px;font-size:28px;line-height:39px;font-weight:700;color:#2b2b2b}
.cta-copy p{position:absolute;left:142px;top:204px;width:440px;font-size:12.8px;line-height:24px;color:#222}

/* testimonials */
.quote-card{position:absolute;top:3212px;width:443px;height:164px;background:#fff;box-shadow:0 2px 12px rgba(0,0,0,.08)}
.quote-card p{position:absolute;left:30px;top:26px;width:390px;font-size:12.4px;line-height:21.7px;color:#333;text-indent:50px}
.quote-card .tail{position:absolute;left:66px;bottom:-14px;width:0;height:0;border-right:26px solid transparent;border-top:14px solid #fff}
.avatar{position:absolute;top:3410px;width:54px;height:54px;border-radius:50%}
.person{position:absolute;top:3417px;font-size:16px;font-weight:700;color:var(--blue)}
.stars{position:absolute;top:3441px;color:var(--star);font-size:13px;letter-spacing:2px}
.slider-arrow{position:absolute;width:32px;height:32px;border-radius:50%;background:#fff;box-shadow:0 1px 6px rgba(0,0,0,.12);display:flex;align-items:center;justify-content:center;font-size:12px;color:#777}

/* clients */
.client-tile{position:absolute;top:3649px;width:170px;height:100px;background:#fff;box-shadow:0 2px 10px rgba(0,0,0,.07);display:flex;align-items:center;justify-content:center;gap:8px;font-size:27px;font-weight:700;color:#2d2d2d}
.client-tile i{width:24px;height:24px;border-radius:50%;display:block}

/* footer */
.site-footer{position:absolute;left:0;top:3840px;width:1200px;height:326px;background:var(--blue)}
.foot-rule{position:absolute;left:141px;width:916px;height:1px;background:rgba(255,255,255,.35)}
.foot-nav a{position:absolute;top:4022px;transform:translateX(-50%);color:#fff;font-size:12.5px;text-decoration:none}
.contact{position:absolute;top:4106px;display:flex;gap:12px;color:#fff;font-size:12.3px;line-height:20px}
.contact .ring{width:28px;height:28px;border-radius:50%;background:#fff;display:flex;align-items:center;justify-content:center;margin-top:4px;flex:none}
.contact b{font-weight:700}
.copyright{position:absolute;left:0;top:4166px;width:1200px;height:50px;background:var(--footer-bottom);color:#fff;font-size:13px;display:flex;align-items:center;justify-content:center}
</style>
</head>
<body>

<!-- HEADER + HERO -->
<section class="hero">
  <div class="brand" style="left:141px;top:22px;font-size:44px;">
    <i class="dot" style="width:46px;height:46px;"></i>kLobbyra
  </div>
  <nav class="nav">
    <a class="active" style="left:611px">Home</a>
    <a style="left:677px">About Us</a>
    <a style="left:761px">Pricing</a>
    <a style="left:834px">Feature</a>
    <a style="left:910px">Blog</a>
  </nav>
  <div class="btn" style="left:958px;top:29px;width:101px;height:40px;">Content</div>

  <div class="photo" role="img" aria-label="Laptop and smartphone showing the kLobbyra location settings dashboard"
       style="left:632px;top:137px;width:525px;height:395px;background:linear-gradient(180deg,#f7f9fc 0%,#dfe4eb 75%,#c9cfd8 100%);border-radius:10px;"></div>

  <h1>kLobbyra Online – Simplifying security one visitor at a time.</h1>
  <p>kLobbyra Online Visitor Management System is a comprehensive platform designed to streamline the process of managing visitors in kLobbyra offers a robust solution to enhance security.</p>
  <div class="btn" style="left:142px;top:414px;width:213px;height:40px;">Start your 15 day free trial</div>
  <div class="btn btn-outline" style="left:372px;top:414px;width:96px;height:40px;">Buy now</div>
</section>
<div class="scroll-badge"><span>
  <svg width="18" height="20" viewBox="0 0 18 20" fill="none" stroke="#fff" stroke-width="1.6"><path d="M3 8l6-6 6 6M3 12l6 6 6-6M3 10h12"/></svg>
</span></div>

<!-- ABOUT -->
<section>
  <svg class="abs" style="left:1064px;top:633px" width="48" height="90" viewBox="0 0 48 90" fill="#b8cfee">
    <circle cx="3" cy="3" r="2"/><circle cx="21" cy="3" r="2"/><circle cx="39" cy="3" r="2"/>
    <circle cx="3" cy="20" r="2"/><circle cx="21" cy="20" r="2"/><circle cx="39" cy="20" r="2"/>
    <circle cx="3" cy="37" r="2"/><circle cx="21" cy="37" r="2"/><circle cx="39" cy="37" r="2"/>
    <circle cx="3" cy="54" r="2"/><circle cx="21" cy="54" r="2"/><circle cx="39" cy="54" r="2"/>
    <circle cx="3" cy="71" r="2"/><circle cx="21" cy="71" r="2"/><circle cx="39" cy="71" r="2"/>
    <circle cx="3" cy="86" r="2"/><circle cx="21" cy="86" r="2"/><circle cx="39" cy="86" r="2"/>
  </svg>
  <svg class="abs" style="left:66px;top:1180px" width="206" height="56" viewBox="0 0 206 56" stroke="#3a7fd6" stroke-width="2.4" stroke-linecap="round" stroke-dasharray="0 7">
    <path d="M2 2H204M2 28H204M2 54H204"/>
  </svg>
  <div class="photo" role="img" aria-label="Professional woman in a blazer overlaid with a city skyline"
       style="left:141px;top:683px;width:386px;height:461px;background:linear-gradient(160deg,#9ba3ad 0%,#d4d8dc 50%,#eef0f2 100%);"></div>
  <div class="photo" role="img" aria-label="Hands typing on a laptop with glowing security icons"
       style="left:378px;top:1008px;width:197px;height:195px;background:linear-gradient(160deg,#3d5a80 0%,#6b87a8 55%,#1e2f46 100%);"></div>

  <h2 class="about-title">About Us</h2>
  <p class="about-copy" style="top:764px;">kLobbyra Online Visitor Management System is dedicated to revolutionizing the way organizations manage their visitors. Our platform offers a modern and efficient solution for businesses, educational institutions, healthcare facilities, and more. With a focus on security, convenience, and professionalism, we strive to provide a seamless experience for both hosts and visitors.</p>
  <p class="about-copy" style="top:941px;">At kLobbyra, we understand the importance of maintaining a secure environment while ensuring a warm welcome for guests. Our system facilitates easy registration, check-in, and tracking of visitors, allowing organizations to maintain control over access to their premises. With</p>
  <div class="btn" style="left:619px;top:1061px;width:109px;height:37px;">Read More</div>
</section>

<!-- FEATURES -->
<section class="features"></section>
<h2 class="section-title" style="top:1380px;">Features</h2>
<div class="title-rule" style="top:1445px;"></div>
<div class="photo" role="img" aria-label="Visitor scanning a QR code on a phone at a tablet check-in kiosk"
     style="left:142px;top:1470px;width:436px;height:457px;border-radius:12px;background:linear-gradient(150deg,#c9a98a 0%,#e9e4df 45%,#f3f5f7 70%,#dfe3e8 100%);"></div>

<div class="feature-card" style="top:1475px;">
  <div class="icon-disc" style="left:18px;top:22px;">
    <svg width="36" height="36" viewBox="0 0 36 36" fill="none" stroke="#222" stroke-width="1.5"><rect x="11" y="4" width="14" height="26" rx="2"/><path d="M15 8h6M14 13h8v8h-8z"/><circle cx="18" cy="26" r="1"/></svg>
  </div>
  <h3 style="left:96px;top:14px;">Contactless Sign-in</h3>
  <p style="left:98px;top:38px;">Lorem ipsum dolor sit amet, consectetur adipiscing elit, sed do eiusmod tempor esw incididunt ut labore et dolore</p>
</div>
<div class="feature-card" style="top:1609px;">
  <h3 style="left:26px;top:14px;">Real-time Alerts</h3>
  <p style="left:28px;top:38px;width:215px;">Lorem ipsum dolor sit amet lorem es consectetur adipiscing elit, sed do eiusmod tempor esw</p>
  <div class="icon-disc" style="left:260px;top:22px;">
    <svg width="36" height="36" viewBox="0 0 36 36" fill="none" stroke="#222" stroke-width="1.5"><rect x="5" y="7" width="26" height="22" rx="2"/><path d="M5 12h26M18 15l-6 10h12z M18 19v3"/></svg>
  </div>
</div>
<div class="feature-card" style="top:1745px;">
  <div class="icon-disc" style="left:18px;top:22px;">
    <svg width="36" height="36" viewBox="0 0 36 36" fill="none" stroke="#222" stroke-width="1.5"><rect x="9" y="5" width="20" height="26" rx="2"/><circle cx="14" cy="12" r="4"/><path d="M12 26l5-6 4 3 5-7M21 10h5M21 14h5"/></svg>
  </div>
  <h3 style="left:96px;top:14px;">Comprehensive Reporting</h3>
  <p style="left:98px;top:38px;">Lorem ipsum dolor sit amet, consectetur es adipiscing elit, sed do eiusmod tempor esw incididunt ut labore et dolore</p>
</div>
<div class="btn" style="left:652px;top:1889px;width:201px;height:39px;">Start Your 15 Day Free Trial</div>

<!-- HOW IT WORKS -->
<h2 class="section-title" style="top:2099px;">How It Works</h2>
<div class="title-rule" style="top:2165px;"></div>

<div class="step-ring" style="left:223px;"></div>
<div class="step-core" style="left:239px;">
  <svg width="50" height="50" viewBox="0 0 50 50" fill="none" stroke="#222" stroke-width="1.6"><rect x="11" y="6" width="28" height="38" rx="3"/><circle cx="25" cy="18" r="5"/><path d="M17 30h16M17 35h16M17 40h10"/></svg>
</div>
<div class="step-num" style="left:222px;">1</div>
<div class="step-title" style="left:163px;">Lorem Ipsum Dolor</div>
<div class="step-copy" style="left:188px;">Lorem ipsum dolor sit consectetuer adipiscing elit, sed diam nonumy nibh euismod tincidunt ut.</div>

<svg class="abs" style="left:412px;top:2262px" width="70" height="24" viewBox="0 0 70 24" fill="none" stroke="#8a8a8a" stroke-width="2"><path d="M2 14Q30 0 64 14"/><path d="M56 8l8 6-9 3"/></svg>

<div class="step-ring" style="left:528px;"></div>
<div class="step-core" style="left:544px;">
  <svg width="50" height="50" viewBox="0 0 50 50" fill="none" stroke="#222" stroke-width="1.6"><path d="M25 6v14M18 13l7-7 7 7M10 18l8 4M40 18l-8 4"/><path d="M14 44l4-14h14l4 14"/><circle cx="25" cy="26" r="3"/></svg>
</div>
<div class="step-num" style="left:528px;">2</div>
<div class="step-title" style="left:468px;">Lorem Ipsum Dolor</div>
<div class="step-copy" style="left:493px;">Lorem ipsum dolor sit consectetuer adipiscing elit, sed diam nonumy nibh euismod tincidunt ut.</div>

<svg class="abs" style="left:718px;top:2260px" width="70" height="24" viewBox="0 0 70 24" fill="none" stroke="#8a8a8a" stroke-width="2"><path d="M2 12Q32 26 64 6"/><path d="M55 5l9 1-3 8"/></svg>

<div class="step-ring" style="left:834px;"></div>
<div class="step-core" style="left:850px;">
  <svg width="50" height="50" viewBox="0 0 50 50" fill="none" stroke="#222" stroke-width="1.6"><circle cx="16" cy="14" r="5"/><circle cx="34" cy="14" r="5"/><circle cx="16" cy="34" r="5"/><circle cx="34" cy="34" r="5"/><path d="M21 14h8M16 19v10M34 19v10"/></svg>
</div>
<div class="step-num" style="left:833px;">3</div>
<div class="step-title" style="left:774px;">Lorem Ipsum Dolor</div>
<div class="step-copy" style="left:799px;">Lorem ipsum dolor sit consectetuer adipiscing elit, sed diam nonumy nibh euismod tincidunt ut.</div>

<div class="btn" style="left:498px;top:2480px;width:203px;height:38px;">Start Your 15 Day Free Trial</div>

<!-- CTA BAND -->
<section class="cta-band">
  <div class="photo" role="img" aria-label="Man in a blue shirt checking in at a tablet kiosk in an office lobby"
       style="left:604px;top:0;width:596px;height:421px;background:linear-gradient(100deg,#d9d6d2 0%,#b9b3ad 45%,#7d6f69 80%,#5a4a48 100%);"></div>
</section>
<div class="cta-copy">
  <h2>Lorem Ipsum Dolor Sit Sed Diam Consectetuer Adipiscing</h2>
  <p>Lorem ipsum dolor sit amet, consectetur adipiscing elit, sed do eiusmod tempor incididunt</p>
  <div class="btn" style="left:142px;top:270px;width:205px;height:37px;">Start Your 15 Day Free Trial</div>
</div>

<!-- TESTIMONIALS -->
<h2 class="section-title" style="top:3111px;">Client Testimonials</h2>
<div class="title-rule" style="top:3177px;"></div>

<div class="slider-arrow" style="left:87px;top:3291px;">&#8249;</div>
<div class="slider-arrow" style="left:1084px;top:3291px;">&#8250;</div>

<div class="quote-card" style="left:144px;">
  <svg class="abs" style="left:22px;top:14px" width="48" height="36" viewBox="0 0 48 36" fill="#c9dcf4"><path d="M2 2h18v16c0 9-6 15-14 16l-1-4c5-1 8-5 8-10H2zM26 2h18v16c0 9-6 15-14 16l-1-4c5-1 8-5 8-10H26z"/></svg>
  <p>Lorem ipsum amet, consectetuer adipisciggng elit, sed diam nonummy nibh euismod tincidunt ut laoreet doore magna aliquam erat volfgutpat. Ut wisi enim ad mifggnim veniam, quis nostrud exerci ese tation ullamcgorper suscipit lobotis nisl &nbsp;aliquip ex ea comhgmodo asa consequat mifggnim veniam</p>
  <div class="tail"></div>
</div>
<div class="quote-card" style="left:619px;">
  <svg class="abs" style="left:22px;top:14px" width="48" height="36" viewBox="0 0 48 36" fill="#c9dcf4"><path d="M2 2h18v16c0 9-6 15-14 16l-1-4c5-1 8-5 8-10H2zM26 2h18v16c0 9-6 15-14 16l-1-4c5-1 8-5 8-10H26z"/></svg>
  <p>Lorem ipsum amet, consectetuer adipisciggng elit, sed diam nonummy nibh euismod tincidunt ut laoreet doore magna aliquam erat volfgutpat. Ut wisi enim ad mifggnim veniam, quis nostrud exerci ese tation ullamcgorper suscipit lobotis nisl &nbsp;aliquip ex ea comhgmodo asa consequat mifggnim veniam</p>
  <div class="tail"></div>
</div>

<div class="avatar" role="img" aria-label="Portrait of a client" style="left:145px;background:linear-gradient(160deg,#8a5a3c,#e4d6cc);"></div>
<div class="person" style="left:213px;">Tunde Okafor</div>
<div class="stars" style="left:213px;">★★★★★</div>
<div class="avatar" role="img" aria-label="Portrait of a client" style="left:614px;background:linear-gradient(160deg,#3a2a22,#a7836b);"></div>
<div class="person" style="left:686px;">Amara Bello</div>
<div class="stars" style="left:686px;">★★★★★</div>

<!-- CLIENTS -->
<h2 class="section-title" style="top:3549px;">Our Clients</h2>
<div class="title-rule" style="top:3616px;"></div>
<div class="slider-arrow" style="left:87px;top:3684px;">&#8249;</div>
<div class="slider-arrow" style="left:1084px;top:3684px;">&#8250;</div>
<div class="client-tile" style="left:144px;"><i style="background:#f5a623"></i>Bexo</div>
<div class="client-tile" style="left:336px;"><i style="background:#e8432d"></i>Tarnfield</div>
<div class="client-tile" style="left:514px;"><i style="background:#2a6fb8"></i>Ovila</div>
<div class="client-tile" style="left:704px;"><i style="background:#36b37e"></i>Quenry</div>
<div class="client-tile" style="left:890px;"><i style="background:#e0477e"></i>Marlo</div>

<!-- FOOTER -->
<footer class="site-footer"></footer>
<div class="brand" style="left:500px;top:3914px;font-size:40px;color:#fff;">
  <i class="dot" style="width:40px;height:40px;"></i>kLobbyra
</div>
<div class="foot-rule" style="top:3989px;"></div>
<nav class="foot-nav">
  <a style="left:224px">Home</a>
  <a style="left:372px">About Us</a>
  <a style="left:523px">Pricing</a>
  <a style="left:670px">Feature</a>
  <a style="left:810px">Blog</a>
  <a style="left:958px">Contact Us</a>
</nav>
<div class="foot-rule" style="top:4073px;"></div>

<div class="contact" style="left:233px;">
  <span class="ring"><svg width="14" height="16" viewBox="0 0 14 16" fill="none" stroke="#1d72d8" stroke-width="1.6"><path d="M7 15s5-5 5-9A5 5 0 0 0 2 6c0 4 5 9 5 9z"/><circle cx="7" cy="6" r="1.6"/></svg></span>
  <div>123, Building Name, Street<br>City, State XY 123456</div>
</div>
<div class="contact" style="left:562px;">
  <span class="ring"><svg width="14" height="14" viewBox="0 0 14 14" fill="none" stroke="#1d72d8" stroke-width="1.6"><path d="M3 1l2 3-1.5 1.5a7 7 0 0 0 5 5L10 9l3 2-1 2c-6 0-11-5-11-11z"/></svg></span>
  <div><b>Phone</b><br>123-456-7890</div>
</div>
<div class="contact" style="left:826px;">
  <span class="ring"><svg width="15" height="12" viewBox="0 0 15 12" fill="none" stroke="#1d72d8" stroke-width="1.6"><rect x="1" y="1" width="13" height="10" rx="1"/><path d="M1 2l6.5 5L14 2"/></svg></span>
  <div><b>Email</b><br>info@klobbyra.com</div>
</div>

<div class="copyright">© 2024 kLobbyra. All Rights Reserved.</div>

</body>
</html>
```